Revolutionary CalmCar Parking Ticket

We are looking for a Brochure Type Web design and a design for a Logo for a brand new company and a product that has no equal anywhere in the world. The product is subject to a Patent Application.
The Company is Bellwether Kerbside Limited and will have a URL of www.lonmeroto.com.au
The designs need to be in Adobe Photo Shop and we are seeking the actual adobe file with unmerged layers.
The product is a digital parking ticket which automatically identifies where a car is parked and if applicable automatically bills the user of the device for the cost of parking for the time the vehicle is parked. The user no longer needs to worry about parking fines, or “feeding” the parking metre. Equally there is no longer any need for those ugly street parking metres.
A picture of the device is attached.
The design needs to impart to the user of the Web Site a feeling of a company which is innovative, designing cutting edge technology, very smart, friendly and sensitive to peoples needs in its area of technology development.
Equally the site needs to be:
a) very simple, uncluttered and clean;
b) such that any user intuitively understands how to use and get what they want.
c) such that the user again intuitively trust the product and the company to deliver a product which does what it indicates it can do;
d) such that it provides confidence that the use of the product will save them money and make sure they don’t get parking fines again and are only charged for the time that they are parked; and
e) such that all understand that they are in control of the operation of the product.
The front page of the Web site needs to provide the user with the following access points:
a) Buy a product;
b) Log into their established account;
c) Make contact with the company;
d) Understand all of the Company Privacy Conditions; and
e) Understand who the company is.
Updates
Please remember that the product is about car parking in any place and one needs to ensure that a site user immediately recognises that by buying the device it makes Car Parking much easier. To put this another way the graphics on the site need to immediately let the user know we are on about car parking made easy.
Target Market(s)
Consumers. Ordinary people who drive cars
Industry/Entity Type
Digital
Logo Text
Ever Calm Tidy Motoring
Number of Pages Required
1 page
Font styles to use
Requirements
Must have
- Must be simple and clean and uncluttered
Nice to have
- Nil
Should not have
- Must not be cluttered

```html
<!DOCTYPE html>
<html lang="en">
<head>
<meta charset="utf-8">
<title>CalmCar – Parking Becomes Easier</title>
<link href="https://fonts.googleapis.com/css2?family=Arimo:wght@400;700&display=swap" rel="stylesheet">
<style>
:root{
  --blue:#1ba6dc;
  --blue-deep:#0a5f8a;
  --green:#6cbf1a;
  --white:#ffffff;
  --ink:#2b2b2b;
  --grey-band:#4a4a4a;
  --dark-band:#1d1d1d;
  --footer:#3a3a3a;
  --muted:#9a9a9a;
}
*{margin:0;padding:0;box-sizing:border-box}
html,body{width:1200px;height:2588px;overflow:hidden}
body{font-family:"Arimo",Arial,sans-serif;color:var(--ink);background:var(--white)}

.site-header{height:80px;display:flex;align-items:center;justify-content:space-between;padding:0 36px;background:var(--white)}
.brand{font-size:28px;font-weight:400;color:var(--ink)}
.account-links{display:flex;align-items:center;font-size:15px;color:var(--ink)}
.account-links span+span{border-left:1px solid var(--muted);margin-left:14px;padding-left:14px}

.hero{position:relative;height:680px;text-align:center;color:var(--white)}
.hero-photo{position:absolute;inset:0;background:linear-gradient(180deg,#2bb1e3 0%,#1790c6 55%,#0b6a9a 100%)}
.hero-content{position:relative;padding-top:200px}
.hero h1{font-size:70px;font-weight:400;letter-spacing:1px}
.hero p{font-size:20px;line-height:27px;width:960px;margin:30px auto 0;text-transform:uppercase}
.btn{display:inline-block;background:var(--green);color:var(--white);font-weight:700;font-size:26px;padding:18px 48px}
.hero .btn{margin-top:48px}
.contact-link{display:block;margin-top:36px;color:var(--green);font-weight:700;font-size:17px}

.who{height:480px;text-align:center;padding-top:70px}
.section-title{font-size:30px;font-weight:400;letter-spacing:1px}
.who p{width:760px;margin:40px auto 0;font-size:14px;line-height:24px;text-align:left}

.band{display:flex;align-items:center;justify-content:center;color:var(--white)}
.what-band{height:120px;background:var(--grey-band)}

.what{height:520px;display:flex}
.device-photo{width:600px;height:520px;background:linear-gradient(135deg,#f2f2f2 0%,#cfcfcf 50%,#8a8a8a 100%)}
.what-text{width:560px;padding:50px 0 0 20px;font-size:14px;line-height:24px}
.learn{display:block;margin-top:14px;color:var(--green);font-weight:700;font-size:14px}

.cta{position:relative;height:340px;text-align:center;color:var(--white)}
.cta-photo{position:absolute;inset:0;background:linear-gradient(180deg,#127fb5 0%,#1ba6dc 50%,#0c5f8c 100%)}
.cta-content{position:relative;padding-top:80px}
.cta h2{font-size:46px;font-weight:400;letter-spacing:1px}
.cta .btn{margin-top:36px}

.contacts-band{height:180px;background:var(--dark-band)}
.site-footer{height:188px;background:var(--footer);display:flex;align-items:center;justify-content:space-between;padding:0 132px;color:var(--white);font-size:17px}
.site-footer b{color:var(--green);font-weight:400;margin-right:14px}
.follow{display:flex;align-items:center;gap:10px}
.follow i{width:40px;height:40px;border-radius:50%;background:#1a1a1a;display:inline-block}
</style>
</head>
<body>
<header class="site-header">
  <div class="brand">CalmCar</div>
  <nav class="account-links"><span>LOG IN</span><span>SIGN UP</span></nav>
</header>

<section class="hero">
  <div class="hero-photo" role="img" aria-label="Blue tinted photo of a driver standing beside parked cars in a car park"></div>
  <div class="hero-content">
    <h1>PARKING BECOMES EASIER</h1>
    <p>Lorem ipsum dolor sit amet, consectetur adipiscing elit, sed do eiusmod tempor incididunt ut labore et dolore magna aliqua. Ut enim ad minim veniam, quis nostrud</p>
    <a class="btn">BUY A PRODUCT</a>
    <a class="contact-link">OR CONTACT US</a>
  </div>
</section>

<section class="who">
  <h2 class="section-title">WHO WE ARE</h2>
  <p>Lorem ipsum dolor sit amet, consectetur adipiscing elit, sed do eiusmod tempor incididunt ut labore et dolore magna aliqua. Ut enim ad minim veniam, quis nostrud exercitation ullamco laboris nisi ut aliquip ex ea commodo consequat. Duis aute irure dolor in reprehenderit in voluptate velit esse cillum dolore eu fugiat nulla pariatur. Excepteur sint occaecat cupidatat non proident, sunt in culpa qui officia deserunt mollit anim id est laborum.</p>
</section>

<div class="band what-band"><h2 class="section-title">WHAT WE DO</h2></div>

<section class="what">
  <div class="device-photo" role="img" aria-label="Photo of the digital parking ticket device lying on a light surface"></div>
  <div class="what-text">
    <p>Lorem ipsum dolor sit amet, consectetur adipiscing elit, sed do eiusmod tempor incididunt ut labore et dolore magna aliqua. Ut enim ad minim veniam, quis nostrud exercitation ullamco laboris nisi ut aliquip ex ea commodo consequat. Duis aute irure dolor in reprehenderit in voluptate velit esse cillum dolore eu fugiat nulla pariatur. Excepteur sint occaecat cupidatat non proident, sunt in culpa qui officia deserunt mollit anim id est laborum. Lorem ipsum dolor sit amet, consectetur adipiscing elit, sed do eiusmod tempor incididunt ut labore et dolore magna aliqua. Ut enim ad minim veniam, quis nostrud exercitation ullamco laboris nisi ut aliquip ex ea commodo consequat. Duis aute irure dolor in reprehenderit in voluptate velit esse cillum dolore eu fugiat nulla pariatur. Excepteur sint occaecat cupidatat non proident, sunt in culpa qui officia deserunt mollit anim id est.</p>
    <a class="learn">LEARN MORE</a>
  </div>
</section>

<section class="cta">
  <div class="cta-photo" role="img" aria-label="Blue tinted photo of an underground car park with parked cars"></div>
  <div class="cta-content">
    <h2>SO WHAT ARE YOU WATING FOR?</h2>
    <a class="btn">BUY A PRODUCT</a>
  </div>
</section>

<div class="band contacts-band"><h2 class="section-title">CONTACTS</h2></div>

<footer class="site-footer">
  <div><b>Email:</b>tidymotor@mailbox.com</div>
  <div><b>Phone:</b>08-555-0142</div>
  <div class="follow"><b>Follow us:</b><i></i><i></i><i></i></div>
</footer>
</body>
</html>
```